Fahrzeugbeschriftung für eine  Autofahrschule
Fahrzeugbeschriftung für eine Autofahrschule
Zielgruppe
Autofahrschule, 18jährige +, also eher junge Leute, die ihren Führerschein machen wollen
Aufgabenstellung
D/E/F bitte bei neuen Vorschlägen weglassen, da es mir nicht so gut gefällt, wenn auf dem Fahrzeug vermerkt.
Worauf legen Sie bei Ihrem Design besonderen Wert? Modernes und anspruchsvolles Design, nicht übertrieben gross, unter Berücksichtigung bereits vorhandenem Design auf dem Fahrzeug, aber nicht zwingend (ausser ,,Rudel K''
Welchen Text möchten Sie in Ihrem Design? ,,kolbeck's fahrschule'' oder ,,Kolbeck's Fahrschule''
,,deutsch/englisch/französisch''
Das Fahrzeug ist ein Brenta Q70, T-Linie, schwarz und hat bereits ein Design in blau. Dieses Design kann übernommen und ergänzt werden, oder ersetzt werden. Hingegen sollte das Logo ,,Rudel K'' bleiben wo es ist (C-Säule links und rechts, siehe Fotos)

```html
<!DOCTYPE html>
<html lang="de">
<head>
<meta charset="utf-8">
<title>Kolbeck´s Fahrschule – Fahrzeugbeschriftung</title>
<link rel="stylesheet" href="https://fonts.googleapis.com/css2?family=Parisienne&display=swap">
<style>
  :root {
    --bg: #333333;
    --ink: #ffffff;
  }
  html, body {
    margin: 0;
    padding: 0;
    overflow: hidden;
  }
  .canvas {
    position: relative;
    width: 929px;
    height: 1200px;
    background: var(--bg);
    overflow: hidden;
  }
  .label-frame {
    position: absolute;
    left: 178px;
    top: 354px;
    width: 456px;
    height: 290px;
    box-sizing: border-box;
    border: 1.5px solid var(--ink);
  }
  .school-name {
    position: absolute;
    left: 254px;
    top: 438px;
    margin: 0;
    font-family: "Parisienne", cursive;
    font-weight: 400;
    font-size: 35px;
    line-height: 1;
    color: var(--ink);
    white-space: nowrap;
  }
  .phone {
    position: absolute;
    left: 257px;
    top: 537px;
    margin: 0;
    font-family: "Helvetica Neue", Helvetica, Arial, sans-serif;
    font-size: 16px;
    line-height: 1;
    color: var(--ink);
    white-space: nowrap;
  }
</style>
</head>
<body>
  <main class="canvas">
    <div class="label-frame"></div>
    <h1 class="school-name">Kolbeck´s Fahrschule</h1>
    <p class="phone">Tel. 077 318 52 64</p>
  </main>
</body>
</html>
```